Expanding Training Company needs a powerpoint template to deliver a consistent professional image

We want to start with a ppt template that is clean and flexible.
We are a small training organisation focusing on personal effectiveness, leadership, management and change. The MD is a New Zealander living in the United Kingdom and loves the idea of the clean green image that NZ has and wants the PowerPoint template to reflect that. We are pragmatic in what we do - everything comes back to performance improvement. Our clients are big players and our presentations need to be as clean, and as professional as theirs. We need a template that is versatile and can have their logos added as necessary.
Our training tends to be very current and as such we would like to use a lot of images and less words/bullets. We have company colours, logos and fonts that we are happy with and will continue to use.

Here are our company values to give you a sense of what we are about…

As a learning organisation we are always looking to continually improve and renew, our material, ideas, and methods, and are continually on the look out for new techniques, interventions and applications that provide measurable results to our clients.

We think life is about people and relationships, and we are prepared to walk away if people don't keep their word, are untrustworthy or lack integrity, as life is just too short to work with arses.
And because we are not arses we admit when we are wrong and make good on our commitments.

For our clients its all about performance and training is a performance enhancer, we aim to provide training excellence tin all its guises that delivers performance and happy clients.

We harness the value of the team, we believe in Interdependence.

We make life easier for our clients and each other.

Flexibility, innovation and future focus/vision are what our clients can count on us for.

Work is one of many of life's great facilitators, we recognise and value the others - its not just about work.

Industry/Entity Type

It Company

Other font styles liked:
• Avenir Next

Colors
abd037
9bcb3c

Requirements
Must have
• A clean look with multiple options for inserting images, tables, videos, text boxes etc
• copyright information
Nice to have
• Slide masters

```html
<!DOCTYPE html>
<html lang="en">
<head>
<meta charset="utf-8">
<title>Fernline Training – Presentation Template Overview</title>
<link href="https://fonts.googleapis.com/css2?family=Lato:ital,wght@0,300;0,400;0,700;0,900;1,400&display=swap" rel="stylesheet">
<style>
:root{
  --bg:#3b3b3b;
  --lime:#9bcb3c;
  --lime-2:#abd037;
  --green:#2a9d48;
  --green-deep:#1f8a3c;
  --ink:#8a8a8a;
  --white:#ffffff;
  --sky:#1e9ad6;
  --navy:#0d3f73;
}
*{margin:0;padding:0;box-sizing:border-box}
html,body{width:1200px;height:890px;overflow:hidden;background:var(--bg);font-family:"Lato",sans-serif}
.canvas{position:relative;width:1200px;height:890px}
.slide{position:absolute;background:var(--white);overflow:hidden}
.slide.green{background:linear-gradient(135deg,var(--lime-2),var(--lime) 70%,#8cc03a)}
.w1{width:288px;height:166px}
.c1{left:8px}.c2{left:306px}.c3{left:602px}.c4{left:899px}
.r1{top:10px}.r2{top:189px}.r3{top:362px}.r4{top:536px}.r5{top:712px}

.foot{position:absolute;left:8px;right:8px;bottom:12px;height:1px;background:var(--green)}
.green .foot{background:rgba(255,255,255,.7)}
.pg{position:absolute;right:8px;bottom:4px;width:11px;height:7px;background:var(--green);color:var(--white);font-size:4px;line-height:7px;text-align:center}
.green .pg{background:var(--green-deep)}
.logo{position:absolute;left:10px;bottom:6px;display:flex;align-items:center;gap:3px;color:var(--green);font-size:8px;font-weight:400;letter-spacing:.2px}
.logo i{display:block;width:8px;height:8px;border-radius:50%;background:currentColor}
.green .logo,.logo.light{color:var(--white)}
.logo.top{top:6px;bottom:auto;left:auto;right:10px}

.h-small{font-size:5.4px;font-weight:700;color:var(--green)}
.body{font-size:4.2px;line-height:6px;color:var(--ink)}
.title{font-size:10px;line-height:12px;font-weight:700;color:var(--green)}
.abs{position:absolute}
.photo{position:absolute}
.blue{background:linear-gradient(160deg,#8fd6f5,var(--sky) 45%,var(--navy))}
.num{display:inline-block;width:9px;height:9px;border-radius:50%;background:var(--green);color:#fff;font-size:3.6px;line-height:9px;text-align:center;margin-right:5px;vertical-align:middle}
.num.soft{background:#b7dc86}
.list li{list-style:none;font-size:4.2px;color:var(--ink);margin-bottom:10px;display:flex;align-items:center}

/* hero */
.hero{left:7px;top:361px;width:592px;height:340px;background:linear-gradient(120deg,#a9cf3a,#9bcb3c 50%,#86b93a)}
.hero .brand{position:absolute;left:160px;top:120px;display:flex;align-items:center;gap:14px;color:#fff}
.hero .brand i{width:64px;height:64px;border-radius:50%;background:#fff;display:block}
.hero .brand span{font-size:46px;line-height:40px;font-weight:300}
.hero .rule{position:absolute;left:150px;right:-8px;top:229px;height:3px;background:#fff}
.hero h1{position:absolute;left:156px;top:284px;color:#fff;font-size:23px;font-weight:400;letter-spacing:.3px}
</style>
</head>
<body>
<main class="canvas">

<!-- Row 1 -->
<section class="slide w1 c1 r1">
  <div class="abs h-small" style="left:12px;top:14px">About Profile</div>
  <p class="abs body" style="left:12px;top:22px;width:60px;font-size:3.4px;line-height:5px">Our profile covers who we are, what we teach and why it works. We build skills that last and lift real team performance across every level of the business, day in and day out.</p>
  <div class="photo" role="img" aria-label="Portrait of a presenter in a suit" style="left:78px;top:10px;width:110px;height:150px;background:linear-gradient(180deg,#d8d8d8,#7b7b7b)"></div>
  <div class="abs" style="left:180px;top:0;width:108px;height:166px;background:var(--lime)"></div>
  <div class="abs" style="left:196px;top:20px;color:#fff;font-size:10px;font-weight:700">Who I'm?</div>
  <p class="abs body" style="left:198px;top:42px;width:80px;color:#fff;font-style:italic">A short note about the speaker goes here, with the main skills and the story that brings them to the room today.</p>
  <div class="foot"></div><div class="pg">02</div>
  <div class="logo"><i></i>fernline training</div>
</section>

<section class="slide w1 c2 r1">
  <div class="abs title" style="left:14px;top:34px">Triangle<br>Shape in<br>Inforgraphics</div>
  <p class="abs body" style="left:14px;top:80px;width:64px">Short note on the chart, what it shows and why it matters to the group.</p>
  <svg class="abs" style="left:92px;top:28px" width="110" height="110" viewBox="0 0 110 110" aria-hidden="true">
    <polygon points="55,8 30,52 80,52" fill="#2fa84f"/>
    <polygon points="30,52 80,52 55,94" fill="#1f7f3a"/>
    <polygon points="30,52 55,94 5,94" fill="#2a9d48"/>
    <polygon points="80,52 105,94 55,94" fill="#8cc63f"/>
    <g fill="#fff" font-family="Lato,sans-serif" font-size="4.5" font-weight="700" text-anchor="middle">
      <text x="55" y="42">Triangle 1</text><text x="55" y="72">Triangle 2</text>
      <text x="30" y="88">Triangle 3</text><text x="80" y="88">Triangle 4</text>
    </g>
  </svg>
  <div class="abs h-small" style="left:205px;top:30px">About Graph Head</div>
  <p class="abs body" style="left:205px;top:38px;width:72px">Explain the graph in a few lines. Keep it short and clear so the room sees the key point at once.</p>
  <div class="foot"></div><div class="pg">02</div>
  <div class="logo"><i></i>fernline training</div>
</section>

<section class="slide w1 c3 r1">
  <div class="abs title" style="left:14px;top:34px">Circle<br>Shape in<br>Inforgraphics</div>
  <p class="abs body" style="left:14px;top:74px;width:62px">Short note on the chart and the one point it makes.</p>
  <svg class="abs" style="left:100px;top:44px" width="100" height="100" viewBox="0 0 100 100" aria-hidden="true">
    <circle cx="50" cy="50" r="46" fill="#2a9d48"/>
    <circle cx="50" cy="50" r="40" fill="#9ed17c"/>
    <circle cx="62" cy="8" r="6" fill="#8cc63f" stroke="#fff" stroke-width="2"/>
  </svg>
  <div class="photo" role="img" aria-label="Two colleagues smiling, framed in a circle" style="left:110px;top:54px;width:80px;height:80px;border-radius:50%;background:linear-gradient(180deg,#e9e9e9,#6f6f6f)"></div>
  <svg class="abs" style="left:160px;top:30px" width="45" height="20" aria-hidden="true"><polyline points="2,19 2,2 45,2" fill="none" stroke="#2a9d48" stroke-width=".8"/></svg>
  <div class="abs h-small" style="left:202px;top:30px">About Circle Head</div>
  <p class="abs body" style="left:202px;top:38px;width:76px">Use the circle to focus on one idea. Add a photo, a short line and a clear link to the talk. Keep each point brief, bold and easy to read from the back of the room.</p>
  <div class="foot"></div><div class="pg">02</div>
  <div class="logo"><i></i>fernline training</div>
</section>

<section class="slide w1 c4 r1 green">
  <div class="abs" style="left:84px;top:42px;display:flex;align-items:center;gap:8px;color:#fff">
    <i style="display:block;width:40px;height:40px;border-radius:50%;background:#fff"></i>
    <span style="font-size:22px;line-height:19px;font-weight:300">fernline<br>training</span>
  </div>
  <div class="abs" style="left:80px;right:0;top:92px;height:2px;background:#fff"></div>
  <div class="abs" style="left:0;right:0;top:100px;text-align:center;color:#fff;font-size:14px;font-weight:700">SECTION SLIDE TITLE  HERE</div>
  <p class="abs body" style="left:50px;right:30px;top:120px;color:#fff;text-align:center;font-size:5px;line-height:9px">A short line that sets up the section and tells the room what comes next.</p>
  <div class="pg">02</div>
</section>

<!-- Row 2 -->
<section class="slide w1 c1 r2">
  <div class="abs h-small" style="left:20px;top:18px">About Portfolio Head</div>
  <p class="abs body" style="left:20px;top:26px;width:68px">Show a recent project with a few clear lines on the aim and the result for the client.</p>
  <p class="abs body" style="left:20px;top:86px;width:68px">Add a second short note to close the story with one strong fact.</p>
  <div class="photo blue" role="img" aria-label="Collage of business people shaking hands in front of a globe" style="left:94px;top:17px;width:186px;height:124px"></div>
  <div class="abs" style="left:141px;top:17px;width:3px;height:124px;background:#fff"></div>
  <div class="abs" style="left:144px;top:42px;width:95px;height:3px;background:#fff"></div>
  <div class="abs" style="left:237px;top:17px;width:3px;height:124px;background:#fff"></div>
  <div class="foot"></div><div class="pg">02</div>
  <div class="logo"><i></i>fernline training</div>
</section>

<section class="slide w1 c2 r2">
  <div class="abs h-small" style="left:20px;top:18px">About Portfolio Head</div>
  <p class="abs body" style="left:20px;top:26px;width:64px">Show a recent project with a few clear lines on the aim and the result for the client.</p>
  <p class="abs body" style="left:20px;top:86px;width:64px">Add a second short note to close the story with one strong fact.</p>
  <svg class="abs" style="left:110px;top:10px" width="170" height="135" viewBox="0 0 170 135" role="img" aria-label="Business people shaking hands, set inside a triangle">
    <defs><linearGradient id="tri-sky" x1="0" y1="0" x2="0" y2="1"><stop offset="0" stop-color="#8fd6f5"/><stop offset=".5" stop-color="#1e9ad6"/><stop offset="1" stop-color="#0d3f73"/></linearGradient></defs>
    <polygon points="85,4 166,130 4,130" fill="#fff" stroke="#d9d9d9" stroke-width="1"/>
    <polygon points="85,10 159,127 11,127" fill="url(#tri-sky)"/>
  </svg>
  <div class="foot"></div><div class="pg">02</div>
  <div class="logo"><i></i>fernline training</div>
</section>

<section class="slide w1 c3 r2" style="background:linear-gradient(180deg,#ececec,#cfcfcf)">
  <div class="photo" role="img" aria-label="Faded city skyline" style="left:0;top:0;width:288px;height:166px;background:linear-gradient(180deg,#f2f2f2 0%,#d6d6d6 60%,#bdbdbd 100%)"></div>
  <svg class="abs" style="left:70px;top:24px" width="150" height="110" viewBox="0 0 150 110" aria-hidden="true">
    <polygon points="70,6 130,96 18,96" fill="#3c3c3c"/>
    <polygon points="90,4 148,96 36,96" fill="#a8a8a8"/>
    <polygon points="75,20 140,110 10,110" fill="#1f9a46"/>
  </svg>
  <div class="abs" style="left:115px;top:76px;width:60px;text-align:center;color:#fff;font-size:4.6px;font-weight:700;line-height:6px">About<br>Section Head</div>
  <p class="abs body" style="left:112px;top:90px;width:66px;color:#fff;text-align:center;font-size:3.8px;line-height:5px">Sum up the section in a few words and lead into the next part of the talk with care.</p>
  <div class="foot"></div><div class="pg">02</div>
  <div class="logo"><i></i>fernline training</div>
</section>

<section class="slide w1 c4 r2 green">
  <div class="photo" role="img" aria-label="Faint city skyline under green tint" style="left:0;top:0;width:288px;height:166px;background:linear-gradient(180deg,rgba(255,255,255,.08),rgba(0,0,0,.06))"></div>
  <p class="abs" style="left:24px;top:64px;width:200px;color:#fff;font-style:italic;font-size:9.5px;line-height:15px">Put a short quote here that sums up the idea and stays with the room long after.</p>
  <div class="pg">02</div>
  <div class="logo"><i></i>fernline training</div>
</section>

<!-- Hero -->
<section class="slide hero" role="img" aria-label="Two smiling business people shaking hands under a green tint">
  <div class="brand"><i></i><span>fernline<br>training</span></div>
  <div class="rule"></div>
  <h1>SECTION SLIDE TITLE HERE</h1>
</section>

<!-- Row 3 right -->
<section class="slide w1 c3 r3">
  <div class="abs title" style="left:14px;top:30px;font-size:9.5px">PHONE DISPLAY<br>HEAD</div>
  <p class="abs body" style="left:14px;top:60px;width:66px">Show the app or site on a phone with a short note on what it does.</p>
  <div class="photo" role="img" aria-label="Hand holding a smartphone showing an app screen" style="left:110px;top:34px;width:64px;height:130px;border-radius:12px 12px 0 0;background:linear-gradient(160deg,#f5f5f5,#cfcfcf)"></div>
  <div class="abs" style="left:120px;top:52px;width:44px;height:72px;background:linear-gradient(180deg,#1c3a5c,#0d2035)"></div>
  <div class="abs h-small" style="left:182px;top:26px">About  Head</div>
  <p class="abs body" style="left:182px;top:34px;width:96px">A short line on the main feature and how it helps people do better work.</p>
  <ul class="abs list" style="left:182px;top:68px">
    <li><span class="num soft">01</span>Short point about a key feature.</li>
    <li><span class="num">02</span>Short point about a key feature.</li>
    <li><span class="num">03</span>Short point about a key feature.</li>
  </ul>
  <div class="foot"></div><div class="pg">02</div>
  <div class="logo"><i></i>fernline training</div>
</section>

<section class="slide w1 c4 r3">
  <div class="abs" style="left:-60px;top:-40px;width:190px;height:196px;border-radius:50%;background:var(--green)"></div>
  <div class="abs" style="left:14px;top:42px;color:#fff;font-size:9.5px;line-height:12px;font-weight:700">PHONE DISPLAY<br>HEAD</div>
  <p class="abs body" style="left:14px;top:76px;width:64px;color:#fff">Show the app or site with a short note on what it does.</p>
  <div class="abs h-small" style="left:142px;top:26px">About  Head</div>
  <p class="abs body" style="left:142px;top:34px;width:136px">A short line on the main feature and how it helps people do better work each day. Keep it clear, keep it brief and let the screen tell the rest.</p>
  <ul class="abs list" style="left:142px;top:76px">
    <li><span class="num soft">01</span>Short point about a key feature.</li>
    <li><span class="num">02</span>Short point about a key feature.</li>
    <li><span class="num">03</span>Short point about a key feature.</li>
  </ul>
  <div class="foot"></div><div class="pg">02</div>
  <div class="logo"><i></i>fernline training</div>
</section>

<!-- Row 4 right -->
<section class="slide w1 c3 r4">
  <div class="abs title" style="left:14px;top:30px;font-size:9.5px">THREE COLOUMN<br>LAYOUT</div>
  <p class="abs body" style="left:14px;top:60px;width:62px">Three images side by side with a short note under each one.</p>
  <div class="photo blue" role="img" aria-label="Businessman standing on a globe" style="left:104px;top:28px;width:56px;height:100px"></div>
  <div class="photo blue" role="img" aria-label="Business people walking on blue ground" style="left:164px;top:28px;width:56px;height:100px"></div>
  <div class="photo blue" role="img" aria-label="Business people walking in motion" style="left:224px;top:28px;width:56px;height:100px"></div>
  <p class="abs body" style="left:104px;top:133px;width:56px">Short caption for image one</p>
  <p class="abs body" style="left:164px;top:133px;width:56px">Short caption for image two</p>
  <p class="abs body" style="left:224px;top:133px;width:56px">Short caption for image three</p>
  <div class="foot"></div><div class="pg">02</div>
  <div class="logo"><i></i>fernline training</div>
</section>

<section class="slide w1 c4 r4">
  <div class="photo blue" role="img" aria-label="Business people on a blue globe, shown in a large circle" style="left:-40px;top:-30px;width:170px;height:170px;border-radius:50%"></div>
  <svg class="abs" style="left:58px;top:60px" width="74" height="66" aria-hidden="true">
    <circle cx="40" cy="32" r="31" fill="#2a9d48" stroke="#fff" stroke-width="1.2"/>
    <polygon points="8,44 14,30 20,48" fill="#2a9d48"/>
  </svg>
  <p class="abs body" style="left:68px;top:76px;width:60px;color:#fff;text-align:center;font-size:3.8px;line-height:5.5px">One short line that explains the image and the point it makes.</p>
  <div class="abs h-small" style="left:142px;top:34px">About  Head</div>
  <p class="abs body" style="left:142px;top:42px;width:136px">A short line on the main feature and how it helps people do better work each day.</p>
  <ul class="abs list" style="left:142px;top:74px">
    <li><span class="num soft">01</span>Short point about a key feature.</li>
    <li><span class="num">02</span>Short point about a key feature.</li>
    <li><span class="num">03</span>Short point about a key feature.</li>
  </ul>
  <div class="foot"></div><div class="pg">02</div>
  <div class="logo light" style="color:#fff"><i></i>fernline training</div>
</section>

<!-- Row 5 -->
<section class="slide w1 c1 r5">
  <div class="abs h-small" style="left:20px;top:22px">About Portfolio Head</div>
  <p class="abs body" style="left:20px;top:30px;width:124px">Show a recent project with a few clear lines on the aim, the work done and the result for the client. Add one strong fact.</p>
  <div class="abs h-small" style="left:20px;top:76px">About Portfolio Head</div>
  <p class="abs body" style="left:20px;top:84px;width:124px">Show a second project with a few clear lines on the aim, the work done and the result for the client.</p>
  <div class="photo blue" role="img" aria-label="Business people standing on a globe" style="left:152px;top:30px;width:130px;height:88px"></div>
  <div class="foot"></div><div class="pg">02</div>
  <div class="logo"><i></i>fernline training</div>
</section>

<section class="slide w1 c2 r5">
  <div class="abs" style="left:0;top:4px;width:2px;height:16px;background:var(--green)"></div>
  <div class="abs h-small" style="left:6px;top:9px;font-size:7px">Our Products</div>
  <div class="logo top"><i></i>fernline training</div>
  <div class="photo blue" role="img" aria-label="Businessman in front of a globe" style="left:0;top:28px;width:94px;height:138px"></div>
  <div class="abs" style="left:94px;top:28px;width:110px;height:138px;background:var(--lime)"></div>
  <svg class="abs" style="left:130px;top:46px" width="40" height="40" aria-hidden="true">
    <circle cx="20" cy="20" r="16" fill="none" stroke="rgba(255,255,255,.4)" stroke-width="1.5"/>
    <path d="M20 4 A16 16 0 1 1 4.8 15" fill="none" stroke="#fff" stroke-width="1.5"/>
    <text x="20" y="23" fill="#fff" font-family="Lato,sans-serif" font-size="8" text-anchor="middle">80%</text>
  </svg>
  <p class="abs body" style="left:106px;top:96px;width:90px;color:#fff">A short line on the product and what it gives the client.</p>
  <p class="abs body" style="left:106px;top:118px;width:90px;color:#fff">A short line on the result it brings.</p>
  <p class="abs body" style="left:106px;top:136px;width:90px;color:#fff">A short line on the next step.</p>
  <div class="photo blue" role="img" aria-label="Business people walking" style="left:204px;top:28px;width:84px;height:138px"></div>
</section>

<section class="slide w1 c3 r5">
  <div class="abs" style="left:0;top:4px;width:2px;height:16px;background:var(--green)"></div>
  <div class="abs h-small" style="left:6px;top:10px">Logo Section here</div>
  <div class="logo top"><i></i>fernline training</div>
  <div class="abs" style="left:22px;top:38px;width:22px;height:22px;border-radius:50%;background:#2f5fa8"></div>
  <div class="abs" style="left:22px;top:78px;width:22px;height:22px;background:#2f5fa8"></div>
  <div class="abs" style="left:20px;top:120px;width:26px;height:14px;background:#d22a2a"></div>
  <p class="abs body" style="left:64px;top:36px;width:94px;font-size:3.6px;line-height:5px">Client name and a short line on the work we did together and the results.</p>
  <p class="abs body" style="left:64px;top:78px;width:94px;font-size:3.6px;line-height:5px">Client name and a short line on the work we did together and the results.</p>
  <p class="abs body" style="left:64px;top:118px;width:94px;font-size:3.6px;line-height:5px">Client name and a short line on the work we did together and the results.</p>
  <p class="abs body" style="left:176px;top:36px;width:104px;font-size:3.6px;line-height:5px">Space for more detail on each client, the course we ran for them, how many people took part and the change it made to their team. Keep the tone plain and the facts clear.</p>
  <p class="abs body" style="left:176px;top:92px;width:104px;font-size:3.6px;line-height:5px">Add a short quote from the client or one number that shows the gain in team performance after the course ended.</p>
  <div class="foot"></div><div class="pg">01</div>
</section>

<section class="slide w1 c4 r5">
  <div class="photo" role="img" aria-label="Business people walking, green tinted" style="left:0;top:0;width:134px;height:166px;background:linear-gradient(160deg,#b6dc5a,#8cc33e 60%,#79b23a)"></div>
  <p class="abs" style="left:14px;top:74px;width:110px;color:#fff;font-style:italic;font-size:4.8px;line-height:7px">Put a short line here about the team and how we work with our clients to get real results.</p>
  <div class="logo top"><i></i>fernline training</div>
  <div class="abs" style="left:142px;top:36px;color:var(--green);font-size:8px;font-weight:300">01</div>
  <div class="abs h-small" style="left:158px;top:37px">About  One</div>
  <p class="abs body" style="left:158px;top:44px;width:122px">A short line on the first point and why it matters.</p>
  <div class="abs" style="left:142px;top:74px;color:var(--green);font-size:8px;font-weight:300">02</div>
  <div class="abs h-small" style="left:158px;top:75px">About  Two</div>
  <p class="abs body" style="left:158px;top:82px;width:122px">A short line on the second point and why it matters.</p>
  <div class="abs" style="left:142px;top:110px;color:var(--green);font-size:8px;font-weight:300">03</div>
  <div class="abs h-small" style="left:158px;top:111px">About  Three</div>
  <p class="abs body" style="left:158px;top:118px;width:122px">A short line on the third point and why it matters.</p>
  <div class="foot" style="left:134px"></div><div class="pg">02</div>
</section>

</main>
</body>
</html>
```